Law Office Business Card

We need a business card design to include the following information:
Name of Firm: Brennick Law Group, P.A.
Address: 4627 Sandlot Ave, Ste 208, West Palm Beach, FL 33409
Phone: 561-555-0148
Fax: 561-555-0193
Website: http://www.tbrennicklaw.example

We Need a place for the Person's name and email address. Please start with the following:
Lorna K. Dwyer, Esq.
lorna@tbrennicklaw.example

```html
<!DOCTYPE html>
<html lang="en">
<head>
<meta charset="utf-8">
<title>Brennick Law Group – Business Card</title>
<link rel="stylesheet" href="https://fonts.googleapis.com/css2?family=Cinzel:wght@400&family=Open+Sans:wght@400&display=swap">
<style>
  :root {
    --backdrop: #2b2725;
    --card-brown: #5d4e45;
    --card-white: #fbfaf8;
    --ink-light: #f4efe9;
    --ink-bronze: #8c7b6d;
    --ink-dark: #3b332e;
    --rule: #9a8a7d;
  }
  * { margin: 0; padding: 0; box-sizing: border-box; }
  html, body { width: 1200px; height: 1200px; overflow: hidden; }
  body { background: var(--backdrop); position: relative; font-family: "Open Sans", sans-serif; }

  .card {
    position: absolute;
    width: 660px;
    height: 378px;
    box-shadow: 0 10px 24px rgba(0,0,0,0.45);
  }

  /* Reverse side: contact details */
  .card--contact { left: 140px; top: 150px; background: var(--card-brown); color: var(--ink-light); }
  .contact-frame {
    position: absolute;
    left: 250px; top: 120px;
    width: 290px; height: 150px;
  }
  .contact-frame__top {
    position: absolute; left: 150px; top: 0; width: 140px; height: 40px;
    border-top: 1.5px solid var(--ink-light); border-right: 1.5px solid var(--ink-light);
  }
  .contact-frame__left {
    position: absolute; left: 0; top: 74px; width: 16px; height: 78px;
    border-left: 1.5px solid var(--ink-light); border-bottom: 1.5px solid var(--ink-light);
  }
  .person-name {
    position: absolute; left: 8px; top: 32px;
    font-family: "Cinzel", serif; font-size: 21px; letter-spacing: 0.5px; white-space: nowrap;
  }
  .contact-list { position: absolute; left: 24px; top: 70px; list-style: none; }
  .contact-list li {
    display: flex; align-items: center; gap: 8px;
    font-size: 14px; line-height: 20px; white-space: nowrap;
  }
  .contact-list svg { width: 13px; height: 13px; fill: var(--ink-light); flex: none; }

  /* Front side: firm name and address */
  .card--firm { left: 400px; top: 640px; background: var(--card-white); color: var(--ink-dark); }
  .firm-mark {
    position: absolute; left: 0; right: 0; top: 96px;
    display: flex; flex-direction: column; align-items: center; gap: 14px;
  }
  .firm-mark__square { width: 52px; height: 52px; border: 2px solid var(--ink-bronze); }
  .firm-mark__name {
    font-family: "Cinzel", serif; font-size: 30px; color: var(--ink-bronze);
    letter-spacing: 1px; text-align: center; line-height: 1.15;
  }
  .firm-address {
    position: absolute; left: 0; right: 0; top: 300px;
    display: flex; align-items: center; gap: 10px; padding: 0 0 0 0;
  }
  .firm-address__rule { height: 1.5px; background: var(--rule); flex: 1; }
  .firm-address__rule--short { flex: 0 0 44px; }
  .firm-address__text { font-size: 15px; letter-spacing: 0.3px; white-space: nowrap; }
</style>
</head>
<body>

  <section class="card card--contact" aria-label="Contact side">
    <div class="contact-frame">
      <span class="contact-frame__top"></span>
      <span class="contact-frame__left"></span>
      <h1 class="person-name">Lorna K. Dwyer, Esq.</h1>
      <ul class="contact-list">
        <li>
          <svg viewBox="0 0 16 16" aria-hidden="true"><path d="M2 5c0-2 2-3 6-3s6 1 6 3v1h-3V5H5v1H2zM3 8l2-2h6l2 2v6H3zm5 1.5a2 2 0 1 0 0 4 2 2 0 0 0 0-4z"/></svg>
          <span>561-555-0148</span>
        </li>
        <li>
          <svg viewBox="0 0 16 16" aria-hidden="true"><path d="M4 1h6l2 2v3H4zM1 7h14v6h-3v2H4v-2H1zm4 4v3h6v-3z"/></svg>
          <span>561-555-0193</span>
        </li>
        <li>
          <svg viewBox="0 0 16 16" aria-hidden="true"><path d="M1 3h14v1L8 9 1 4zm0 3 7 5 7-5v7H1z"/></svg>
          <span>lorna@tbrennicklaw.example</span>
        </li>
        <li>
          <svg viewBox="0 0 16 16" aria-hidden="true"><path d="M8 1a7 7 0 1 0 0 14A7 7 0 0 0 8 1zm0 1.5c.8 0 1.7 1.6 2 4H6c.3-2.4 1.2-4 2-4zM6 8h4c0 .5 0 1 0 1.5H6C6 9 6 8.5 6 8zm-3.4 0h2c0 .5 0 1 .1 1.5H2.8A5.5 5.5 0 0 1 2.6 8zm8.8 0h2a5.5 5.5 0 0 1-.2 1.5h-1.9c.1-.5.1-1 .1-1.5zM6.1 11h3.8c-.4 1.6-1.1 2.5-1.9 2.5S6.5 12.6 6.1 11z"/></svg>
          <span>www.tbrennicklaw.example</span>
        </li>
      </ul>
    </div>
  </section>

  <section class="card card--firm" aria-label="Firm side">
    <div class="firm-mark">
      <span class="firm-mark__square"></span>
      <p class="firm-mark__name">Brennick Law<br>Group</p>
    </div>
    <div class="firm-address">
      <span class="firm-address__rule firm-address__rule--short"></span>
      <span class="firm-address__text">4627 Sandlot Ave, Ste 208, West Palm Beach, FL 33409</span>
      <span class="firm-address__rule"></span>
    </div>
  </section>

</body>
</html>
```